Business Card Design for MOTORBLISS, a modern automotive repair and performance shop.

MOTOR=ENGINE
BLISS=JOY

We have just started an automotive repair shop specializing in Asian, European, and domestic vehicle service, repair, fabrication and performance. All the technicians here are manufacturer trained and certified, both by several manufacturers and by KTQ (garage quality league), to include Varenko, Lumaro, Pelvoro, Dravenholt, and Kestrawind.

We are looking for a modern business card, with use of a dark background, like black or dark grey. Use of red, white, grey, and black. Somehow integrate the shop logo into the back ground or into a shield or some type of surround. Maybe even use a silhouette of a vehicle. (top lines of the vehicle) Preferably (2009+lumaro zfx), would like the front of the card to state basics, and back of the card to show what we are capable of.

Target Market(s)

Target market will be customer of all ages, from the younger tuner crowd, to the older vehicle owners.

Industry/Entity Type

Automotive

Contact Information for Business Card

name of business = MotorBliss
address of business = 5128 W. Birchwell Ln, Killeen T.X. 76549
phone# 1-254-555-0193 fax# 1-254-555-0147
website www.motor-bliss.example
email info@motor-bliss.example

Font styles to use
Sans Serif

Requirements
Must have
• Specializing in Asian, European, and domestic vehicle service, repair, fabrication and performance.

This should be on the back of the business card.

```html
<!DOCTYPE html>
<html lang="en">
<head>
<meta charset="utf-8">
<title>MotorBliss Business Card</title>
<link rel="stylesheet" href="https://fonts.googleapis.com/css2?family=Roboto+Condensed:wght@700&display=swap">
<style>
  :root {
    --card-edge: #0d0d0d;
    --card-mid: #2a2a2a;
    --card-glow: #3a3a3a;
    --text-grey: #a6a6a6;
    --brand-grey: #9e9e9e;
    --accent-red: #b01a1e;
    --vehicle-dark: #232323;
    --vehicle-light: #363636;
  }
  * { margin: 0; padding: 0; box-sizing: border-box; }
  html, body {
    width: 1200px;
    height: 702px;
    overflow: hidden;
    background: var(--card-edge);
  }
  .card {
    position: relative;
    width: 1200px;
    height: 702px;
    overflow: hidden;
    font-family: "Roboto Condensed", "Arial Narrow", sans-serif;
    font-weight: 700;
    background: radial-gradient(ellipse 62% 68% at 50% 42%, var(--card-glow) 0%, var(--card-mid) 45%, var(--card-edge) 100%);
  }
  .vehicle-silhouette {
    position: absolute;
    left: 258px;
    top: 222px;
    width: 660px;
    height: 300px;
    border-radius: 150px 150px 70px 70px / 120px 120px 50px 50px;
    background: radial-gradient(ellipse 55% 60% at 50% 50%, var(--vehicle-light) 0%, var(--vehicle-dark) 65%, rgba(35,35,35,0) 100%);
  }
  .brand {
    position: absolute;
    left: 0;
    top: 96px;
    width: 1200px;
    display: flex;
    justify-content: center;
    align-items: center;
    gap: 22px;
  }
  .brand-square {
    width: 56px;
    height: 56px;
    background: var(--brand-grey);
  }
  .brand-name {
    font-size: 108px;
    line-height: 1;
    letter-spacing: 1px;
    color: var(--brand-grey);
  }
  .address {
    position: absolute;
    left: 46px;
    top: 541px;
    font-size: 33px;
    line-height: 44px;
    color: var(--text-grey);
  }
  .contact-list {
    position: absolute;
    left: 727px;
    top: 445px;
    list-style: none;
    font-size: 34px;
    line-height: 44px;
    color: var(--text-grey);
  }
  .contact-label {
    display: inline-block;
    width: 46px;
    color: var(--accent-red);
  }
</style>
</head>
<body>
  <div class="card">
    <div class="vehicle-silhouette" role="img" aria-label="Faint front view of a sports car in the dark background"></div>

    <div class="brand">
      <span class="brand-square"></span>
      <span class="brand-name">MotorBliss</span>
    </div>

    <p class="address">5128 W. Birchwell Ln ste B Killeen,<br>T.X. 76549</p>

    <ul class="contact-list">
      <li><span class="contact-label">P:</span>1-254-555-0193</li>
      <li><span class="contact-label">F:</span>1-254-555-0147</li>
      <li><span class="contact-label">W:</span>www.motor-bliss.example</li>
      <li><span class="contact-label">E:</span>info@motor-bliss.example</li>
    </ul>
  </div>
</body>
</html>
```